KVT Business Cards

We require business cards for our business. We would like a matte black back to the card, with our logo centred in the middle. The front side of the card is open to design.

Target Market(s)

Clients looking for legal services (professional)

Industry/Entity Type

Legal

Contact Information for Business Card

Boris Telemark
Partner
Mobile: 0438 715 642
Email: boris@kvtlaw.co
Website: www.kvtlaw.co
Level 3, 118 Wexbury Street
Sydney NSW 2000

Font styles to use
Other font styles liked:
• Avenir

Colors
f04a50
ffffff
1b1b1b

Requirements
Must have
• Black back with logo included in the centre of the card.
• Our font is Avenir.

```html
<!DOCTYPE html>
<html lang="en">
<head>
<meta charset="utf-8">
<title>KVT Legal – Business Card</title>
<link rel="stylesheet" href="https://fonts.googleapis.com/css2?family=Fira+Sans:wght@400;500;700;800&display=swap">
<style>
  :root {
    --crimson: #c8284e;
    --crimson-deep: #9a1a35;
    --ink: #1b1b1b;
    --matte: #1b1b1b;
    --paper: #ffffff;
    --stage: #3b3b3b;
    --grey-text: #2a2a2a;
  }
  * { box-sizing: border-box; margin: 0; padding: 0; }
  html, body {
    width: 1200px; height: 900px; overflow: hidden;
    background: var(--stage);
    font-family: "Fira Sans", "Helvetica Neue", Arial, sans-serif;
  }
  .canvas {
    width: 1200px; height: 900px;
    display: flex; flex-direction: column; align-items: center; justify-content: center;
    gap: 40px;
  }
  .card {
    position: relative;
    width: 640px; height: 391px;
    overflow: hidden;
    box-shadow: 0 10px 30px rgba(0,0,0,.45);
  }

  /* Back side: matte black */
  .card--back { background: var(--matte); }
  .band { position: absolute; left: 0; right: 0; }
  .card--back .band--top {
    top: 0; height: 22px;
    background: linear-gradient(90deg, var(--crimson-deep) 0%, var(--crimson) 45%, #8f8f8f 62%, #3a0e18 82%, #2a2a2a 100%);
  }
  .card--back .band--bottom {
    bottom: 0; height: 44px;
    background: linear-gradient(90deg, #2a2a2a 0%, #5a1626 30%, #8f8f8f 45%, var(--crimson) 65%, var(--crimson-deep) 100%);
  }
  .back-mark {
    position: absolute; left: 50%; top: 50%;
    transform: translate(-50%, -50%);
    display: flex; align-items: center; gap: 24px;
  }
  .mark-square { display: block; flex: none; }
  .back-mark .mark-square { width: 60px; height: 60px; background: var(--crimson); }
  .back-mark .name {
    font-weight: 800; font-size: 50px; letter-spacing: 1px;
    color: var(--paper); text-transform: uppercase; line-height: 1;
    white-space: nowrap;
  }

  /* Front side */
  .card--front { background: var(--paper); }
  .card--front .band--top {
    top: 0; height: 44px;
    background: linear-gradient(90deg, #e37a90 0%, #d6496a 40%, #8a2a3c 70%, #2a2a2a 100%);
  }
  .card--front .band--bottom {
    bottom: 0; height: 62px;
    background: linear-gradient(90deg, #2a2a2a 0%, #7a2a3a 30%, #d6496a 60%, #e37a90 100%);
  }
  .front-mark {
    position: absolute; left: 44px; top: 168px;
    display: flex; align-items: center; gap: 16px;
  }
  .front-mark .mark-square { width: 38px; height: 38px; background: var(--crimson); }
  .front-mark .name {
    font-weight: 800; font-size: 34px; letter-spacing: .5px;
    color: var(--ink); text-transform: uppercase; line-height: 1;
    white-space: nowrap;
  }
  .divider {
    position: absolute; left: 300px; top: 90px; width: 2px; height: 190px;
    background: linear-gradient(180deg, rgba(200,40,78,0), var(--crimson) 35%, rgba(200,40,78,0));
  }
  .contact {
    position: absolute; left: 330px; top: 92px;
    color: var(--grey-text);
  }
  .contact .person {
    font-weight: 700; font-size: 25px; letter-spacing: 1px;
    color: var(--crimson); text-transform: uppercase; line-height: 1.1;
    white-space: nowrap;
  }
  .contact .role { font-size: 15px; margin-top: 2px; margin-bottom: 14px; }
  .contact ul { list-style: none; }
  .contact li {
    display: flex; align-items: center; gap: 10px;
    font-size: 17px; line-height: 1.45;
  }
  .contact li svg { width: 16px; height: 16px; flex: none; fill: var(--crimson); }
  .contact address {
    font-style: normal; font-size: 17px; line-height: 1.4; margin-top: 14px;
  }
</style>
</head>
<body>
<main class="canvas">

  <section class="card card--back" aria-label="Card back">
    <div class="band band--top" role="img" aria-label="Checkered square border in crimson, black and grey"></div>
    <div class="back-mark">
      <span class="mark-square"></span>
      <span class="name">KVT Legal</span>
    </div>
    <div class="band band--bottom" role="img" aria-label="Checkered square border fading from black to crimson"></div>
  </section>

  <section class="card card--front" aria-label="Card front">
    <div class="band band--top" role="img" aria-label="Checkered square border fading from crimson to black"></div>

    <div class="front-mark">
      <span class="mark-square"></span>
      <span class="name">KVT Legal</span>
    </div>

    <div class="divider"></div>

    <div class="contact">
      <p class="person">Boris Telemark</p>
      <p class="role">Partner</p>
      <ul>
        <li>
          <svg viewBox="0 0 24 24" aria-hidden="true"><path d="M6.6 10.8a15.1 15.1 0 0 0 6.6 6.6l2.2-2.2c.3-.3.7-.4 1-.2 1.1.4 2.3.6 3.6.6.6 0 1 .4 1 1V20c0 .6-.4 1-1 1C10.6 21 3 13.4 3 4c0-.6.4-1 1-1h3.5c.6 0 1 .4 1 1 0 1.3.2 2.5.6 3.6.1.3 0 .7-.2 1z"/></svg>
          <span>0438 715 642</span>
        </li>
        <li>
          <svg viewBox="0 0 24 24" aria-hidden="true"><path d="M2 5h20v14H2zm2 2v.5l8 5 8-5V7l-8 5z"/></svg>
          <span>boris@kvtlaw.co</span>
        </li>
        <li>
          <svg viewBox="0 0 24 24" aria-hidden="true"><circle cx="12" cy="12" r="10"/><path d="M2 12h20M12 2c3 3 3 17 0 20M12 2c-3 3-3 17 0 20" stroke="#fff" stroke-width="1.5" fill="none"/></svg>
          <span>www.kvtlaw.co</span>
        </li>
      </ul>
      <address>Level 3, 118 Wexbury Street<br>Sydney NSW 2000</address>
    </div>

    <div class="band band--bottom" role="img" aria-label="Checkered square border fading from black to crimson"></div>
  </section>

</main>
</body>
</html>
```